don't add new designs, a winner will be choosed A website for mothers about homeopathy

We have a blog www.lottamaus.eu based on WordPress (Wix would be also good) about homeopathy-critique and health issues.
Our logo is a little girl Henrike, the background color green.
It looks somehow good, but we want to be up to date:).
Our goal is to open eyes from propaganda and misinformation on the web. We are all volunteers and invest our time and money for this purpose. Once people like it, we are happy to translate our blog to the English.
Updates

Please, don't submit a new design. we will choose from the designs we already have. Thank you! Added Thursday, July 20, 2017

Target Market(s)

mothers, people reading about health

Industry/Entity Type

Health

Number of Pages Required

3 page

Colors
abd037

Requirements
Must have
• - nice, friendly, evoking positive emotions
• - colorful (see for example how it looks now)
• - a good way how to show up articles (actually, if you open an article, you have to scroll, it appears on the bottom of the page)
• - We need to arrange stuff, where to put "most read", "Category", "contact", "themes" "search" (now, everything is on the right side. if you like it so, ok)
Nice to have
• Everything is in German, but I am happy to translate everything you need.
• The big text is: Lottchen mag keine Kügelchen: Henrike wants no Pellets (the sugar pills of homeopathy)
• "(Nicht nur) homöopathiekritische Informationen für Eltern und alle, die für unsere Kleinen sorgen" - (Not only) Homeopathy-critique Information for Parents and All Who Take Care Of Our Small (Children)
• - there are many of the pictures of Henrike, you can choose the best one. You can find them here https://www.verbund-faktenblick.eu/lottchen-mag-keine-kuegelchen
• - we have also a FB, which could be integrated https://www.facebook.com/lottchenmagkeinekuegelchen/?fref=ts
Should not have
• - a sterile modern look

```html
<!DOCTYPE html>
<html lang="en">
<head>
<meta charset="utf-8">
<title>Lottchen mag keine Kügelchen</title>
<link href="https://fonts.googleapis.com/css2?family=Mulish:wght@400;600;700&family=Open+Sans:wght@400;600&display=swap" rel="stylesheet">
<style>
:root{
  --green:#abd037;
  --green-dark:#8cbf26;
  --green-text:#9ac22c;
  --olive:#5a6b12;
  --ink:#333;
  --muted:#8a8a8a;
  --line:#e4e4e4;
  --page:#eeeeee;
  --white:#ffffff;
  --footer:#4a4a4a;
  --sky:#6aa9d8;
  --sea:#3f9fb3;
  --sand:#c9ad7e;
}
*{box-sizing:border-box;margin:0;padding:0}
html,body{width:1200px;height:2932px;overflow:hidden}
body{position:relative;background:var(--page);font-family:"Open Sans",sans-serif;color:var(--ink)}
.abs{position:absolute}

/* header */
.site-header{left:0;top:0;width:1200px;height:105px;background:var(--white)}
.brand{left:130px;top:30px;display:flex;align-items:center;gap:14px}
.brand-mark{width:44px;height:44px;border-radius:50%;background:var(--green)}
.brand-name{font-family:"Mulish",sans-serif;font-weight:700;font-size:18px;line-height:24px;color:var(--olive);white-space:nowrap}
.main-nav{left:500px;top:32px;display:flex;font-family:"Mulish",sans-serif;font-size:16px}
.main-nav a{color:#555;text-decoration:none;padding:9px 16px;border:2px solid transparent}
.main-nav a.active{color:var(--green-dark);border-color:var(--green)}

/* hero */
.hero{left:0;top:105px;width:1200px;height:600px;overflow:hidden}
.hero-photo{position:absolute;inset:0;background:linear-gradient(180deg,var(--sky) 0%,#a8cde6 38%,var(--sea) 52%,#7bb8a4 60%,var(--sand) 75%,#8a7a52 100%)}
.hero-palms{position:absolute;inset:0;background:linear-gradient(90deg,rgba(47,74,38,.75) 0%,rgba(47,74,38,.2) 25%,rgba(47,74,38,.1) 55%,rgba(47,74,38,.6) 85%,rgba(47,74,38,.8) 100%)}
.hero-badge{left:113px;top:90px;width:352px;height:352px;border-radius:50%;background:var(--green);border:9px solid var(--white);color:var(--white);text-align:center;padding:112px 18px 0}
.hero-badge h1{font-family:"Mulish",sans-serif;font-weight:400;font-size:28px;line-height:34px;white-space:nowrap}
.hero-badge p{font-size:12.5px;line-height:20px;margin:14px 24px 0}
.hero-dots{left:555px;top:478px;display:flex;gap:9px}
.hero-dots span{width:13px;height:13px;border-radius:50%;background:rgba(255,255,255,.8)}
.hero-wave{left:0;top:620px;width:1200px;height:90px}

/* welcome */
.welcome{left:0;top:690px;width:1200px;height:297px;background:var(--white)}
.welcome h2{position:absolute;left:0;width:1200px;top:0;text-align:center;font-family:"Mulish",sans-serif;font-weight:400;font-size:35px;color:var(--olive)}
.welcome p{position:absolute;left:228px;width:744px;top:58px;text-align:center;font-size:15px;line-height:25px;color:var(--muted)}
.btn-outline{position:absolute;left:516px;top:181px;width:162px;height:44px;border:2px solid #555;border-radius:22px;font-family:"Mulish",sans-serif;font-size:16px;line-height:40px;text-align:center;color:#333}
.figure-nurse{left:98px;top:60px;width:107px;height:237px;border-radius:50px 50px 20px 20px;background:linear-gradient(180deg,#f6d36a 0%,#f3dcc4 30%,#ffffff 55%,#cfd7ee 100%)}
.figure-reader{left:938px;top:60px;width:166px;height:237px;border-radius:70px 70px 20px 20px;background:linear-gradient(180deg,#f6d36a 0%,#f3dcc4 35%,#e9c9a5 55%,#d8474a 80%,#f1e6e6 100%)}

/* main content */
.section-title{left:119px;top:1016px;font-family:"Mulish",sans-serif;font-weight:400;font-size:31px;color:#333}
.article-card{left:117px;width:670px;height:293px;background:var(--white);border:1px solid var(--line)}
.article-thumb{position:absolute;left:16px;top:20px;width:297px;height:250px}
.article-body{position:absolute;left:340px;top:20px;width:310px}
.article-body h3{font-family:"Mulish",sans-serif;font-weight:400;font-size:21px;color:var(--green-text);margin-bottom:12px}
.article-body p{font-size:12.5px;line-height:22px;color:var(--muted);margin-bottom:8px}
.article-actions{position:absolute;left:340px;top:228px;width:310px;border-top:1px solid var(--line);padding-top:11px;display:flex;gap:22px;font-family:"Mulish",sans-serif;font-size:12px;color:var(--muted)}
.article-actions .more{color:var(--green-text)}
.article-actions span{display:flex;align-items:center;gap:5px}
.pager{left:386px;top:2632px;display:flex;gap:7px}
.pager span{width:28px;height:28px;border-radius:50%;background:var(--white);border:1px solid #ccc;font-size:13px;line-height:26px;text-align:center;color:#333}
.pager .arrow{background:var(--green);border-color:var(--green)}
.pager .current{background:#333;color:var(--white);border-color:#333}

/* sidebar */
.widget{left:821px;width:262px;background:var(--white);border:1px solid var(--line)}
.widget-about{top:1012px;height:258px;background:linear-gradient(180deg,var(--green) 0%,var(--green-dark) 100%);border:none;color:var(--white);padding:26px 26px}
.widget-about h4{font-family:"Mulish",sans-serif;font-weight:400;font-size:23px;margin-bottom:10px}
.widget-about p{font-size:11.5px;line-height:18px;margin-bottom:10px;opacity:.95}
.btn-ghost{display:inline-block;margin-top:4px;border:2px solid var(--white);padding:6px 22px;font-family:"Mulish",sans-serif;font-weight:700;font-size:13px}
.widget-popular{top:1290px;height:498px}
.widget-head{height:44px;background:var(--green);color:var(--white);font-family:"Mulish",sans-serif;font-size:20px;line-height:44px;padding-left:26px}
.pop-item{display:flex;gap:14px;padding:17px 22px 0;height:113px;border-bottom:1px solid var(--line)}
.pop-item:last-child{border-bottom:none}
.pop-thumb{width:78px;height:72px;flex:none}
.pop-text h5{font-family:"Mulish",sans-serif;font-weight:400;font-size:13px;color:#333;margin-bottom:4px}
.pop-text p{font-size:10px;line-height:13px;color:var(--muted)}
.pop-text .more{font-family:"Mulish",sans-serif;font-size:10px;color:var(--green-text);margin-top:2px}
.widget-news{top:1809px;height:168px;padding:20px 20px}
.widget-news h4{font-family:"Mulish",sans-serif;font-weight:400;font-size:19px;color:#333;margin-bottom:14px}
.field{height:34px;border:1px solid #ccc;font-size:12px;color:#777;padding:8px 12px;margin:0 0 8px 0}
.btn-fill{height:34px;background:var(--green);color:var(--white);text-align:center;font-family:"Mulish",sans-serif;font-weight:700;font-size:14px;line-height:34px}
.widget-tags{top:1995px;height:266px;background:#f2f2f2;padding:16px 20px}
.widget-tags h4{font-family:"Mulish",sans-serif;font-weight:400;font-size:19px;color:#333;margin-bottom:18px}
.tag-list{display:flex;flex-wrap:wrap;gap:6px 4px}
.tag-list span{background:#dedede;font-size:9px;padding:5px 5px;color:#555}
.widget-social{top:2267px;height:341px}
.page-banner{position:relative;height:112px;background:linear-gradient(135deg,#8a9aa8 0%,#c6b68a 60%,#f1c84a 100%)}
.page-banner .name{position:absolute;left:60px;top:6px;font-size:15px;color:var(--white)}
.page-banner .pic{position:absolute;left:8px;top:8px;width:44px;height:44px;background:var(--white)}
.page-btn{position:absolute;top:80px;height:22px;background:var(--white);border:1px solid #ccc;font-size:9px;line-height:20px;padding:0 8px;color:#444}
.feed-item{display:flex;gap:10px;padding:22px 16px 0}
.feed-avatar{width:38px;height:34px;flex:none}
.feed-item p{font-size:10.5px;line-height:16px;color:#333}
.feed-item p small{display:block;color:#4a6fb5;font-size:10px;margin-top:4px}

/* decorative characters */
.char{border-radius:40px}
.char-girl{left:0;top:1974px;width:88px;height:312px;background:linear-gradient(180deg,#f6d36a 0%,#f3dcc4 28%,#9db7e8 55%,#d9e3f6 100%)}
.char-dog{left:1094px;top:2013px;width:106px;height:137px;background:linear-gradient(160deg,#e8a94a 0%,#c98532 100%)}
.char-boy{left:1071px;top:2482px;width:129px;height:293px;background:linear-gradient(180deg,#d9393d 0%,#f6d36a 18%,#f3dcc4 35%,#6cbf5a 60%,#e04a4a 80%,#f3dcc4 100%)}

/* footer */
.footer-wave{left:0;top:2700px;width:1200px;height:90px}
.site-footer{left:0;top:2780px;width:1200px;height:152px;background:var(--footer)}
.foot-nav{position:absolute;left:119px;top:34px;display:flex;gap:26px;font-family:"Mulish",sans-serif;font-size:16px;color:var(--white)}
.copyright{position:absolute;left:119px;top:65px;font-size:12px;color:#aaa}
.social{position:absolute;left:872px;top:40px;display:flex;gap:10px}
.social span{width:33px;height:33px;border-radius:50%;border:2px solid var(--white)}
</style>
</head>
<body>

<header class="site-header abs">
  <div class="brand abs">
    <span class="brand-mark"></span>
    <span class="brand-name">Lottchen mag keine Kügelchen</span>
  </div>
  <nav class="main-nav abs">
    <a class="active">Home</a><a>Articles</a><a>About the Henrike</a><a>Henrike's Shop</a><a>Contact</a>
  </nav>
</header>

<section class="hero abs">
  <div class="hero-photo" role="img" aria-label="Tropical beach with palm trees, sea and blue sky"></div>
  <div class="hero-palms"></div>
  <div class="hero-badge abs">
    <h1>Homeopathy-Critique<br>&amp; Health Issues</h1>
    <p>Class aptent taciti sociosqu ad litora torquent per conubia nostra per inceptos hymenaeos Proin nulla arcu</p>
  </div>
  <div class="hero-dots abs"><span></span><span></span><span></span><span></span></div>
</section>
<svg class="hero-wave abs" viewBox="0 0 1200 90" preserveAspectRatio="none" aria-hidden="true">
  <path d="M0 30 Q600 95 1200 10 L1200 90 L0 90 Z" fill="var(--green)"/>
  <path d="M0 48 Q600 100 1200 30 L1200 90 L0 90 Z" fill="var(--white)"/>
</svg>

<section class="welcome abs">
  <h2>Welcome to the Lottchen!</h2>
  <p>Lottchen and her friend Jonas with her two companions Dog Flocke and Cat Moritz are part of the Faktenblick information network (FIN). In particular, we want to reach parents and their children with our conviction that it does not need pseudomedicine for a natural, healthy growing-up. Lottchen stands for sensible and critical thinking for young and old.</p>
  <span class="btn-outline">READ MORE</span>
  <div class="figure-nurse abs char" role="img" aria-label="Cartoon girl dressed as a nurse holding a syringe"></div>
  <div class="figure-reader abs char" role="img" aria-label="Cartoon girl sitting in a chair reading a book"></div>
</section>

<h2 class="section-title abs">Featured Articles</h2>

<article class="article-card abs" style="top:1071px">
  <div class="article-thumb" role="img" aria-label="Smiling baby" style="background:linear-gradient(135deg,#e9d2c2,#b89a86)"></div>
  <div class="article-body"><h3>Morbi diam mauris viverra</h3>
  <p>ullamcorper est eget tempor cursus neque mi consectetuer mi a ultricies massa est sed nisl Class aptent taciti sociosqu ad litora torquent</p>
  <p>per conubia nostra per inceptos hymenaeos Proin nulla arcu nonummy luctus dictum eget fermentum et lorem iaculis ipsum</p></div>
  <div class="article-actions"><span class="more">READ MORE</span><span>&#9679; COMMENT</span><span>&#10150; SHARE</span></div>
</article>
<article class="article-card abs" style="top:1382px">
  <div class="article-thumb" role="img" aria-label="Newborn baby held in a clinic" style="background:linear-gradient(135deg,#5b7fa3,#d8a890)"></div>
  <div class="article-body"><h3>Morbi diam mauris viverra</h3>
  <p>ullamcorper est eget tempor cursus neque mi consectetuer mi a ultricies massa est sed nisl Class aptent taciti sociosqu ad litora torquent</p>
  <p>per conubia nostra per inceptos hymenaeos Proin nulla arcu nonummy luctus dictum eget fermentum et lorem iaculis ipsum</p></div>
  <div class="article-actions"><span class="more">READ MORE</span><span>&#9679; COMMENT</span><span>&#10150; SHARE</span></div>
</article>
<article class="article-card abs" style="top:1694px">
  <div class="article-thumb" role="img" aria-label="Strawberries and berries" style="background:linear-gradient(135deg,#d8262e,#5a1a3a)"></div>
  <div class="article-body"><h3>Morbi diam mauris viverra</h3>
  <p>ullamcorper est eget tempor cursus neque mi consectetuer mi a ultricies massa est sed nisl Class aptent taciti sociosqu ad litora torquent</p>
  <p>per conubia nostra per inceptos hymenaeos Proin nulla arcu nonummy luctus dictum eget fermentum et lorem iaculis ipsum</p></div>
  <div class="article-actions"><span class="more">READ MORE</span><span>&#9679; COMMENT</span><span>&#10150; SHARE</span></div>
</article>
<article class="article-card abs" style="top:2005px">
  <div class="article-thumb" role="img" aria-label="Bumblebee on a purple thistle flower" style="background:linear-gradient(135deg,#4f6a2c,#8a4a8a)"></div>
  <div class="article-body"><h3>Morbi diam mauris viverra</h3>
  <p>ullamcorper est eget tempor cursus neque mi consectetuer mi a ultricies massa est sed nisl Class aptent taciti sociosqu ad litora torquent</p>
  <p>per conubia nostra per inceptos hymenaeos Proin nulla arcu nonummy luctus dictum eget fermentum et lorem iaculis ipsum</p></div>
  <div class="article-actions"><span class="more">READ MORE</span><span>&#9679; COMMENT</span><span>&#10150; SHARE</span></div>
</article>
<article class="article-card abs" style="top:2317px">
  <div class="article-thumb" role="img" aria-label="Potted plant by a window" style="background:linear-gradient(135deg,#e8e4dc,#4c6b34)"></div>
  <div class="article-body"><h3>Morbi diam mauris viverra</h3>
  <p>ullamcorper est eget tempor cursus neque mi consectetuer mi a ultricies massa est sed nisl Class aptent taciti sociosqu ad litora torquent</p>
  <p>per conubia nostra per inceptos hymenaeos Proin nulla arcu nonummy luctus dictum eget fermentum et lorem iaculis ipsum</p></div>
  <div class="article-actions"><span class="more">READ MORE</span><span>&#9679; COMMENT</span><span>&#10150; SHARE</span></div>
</article>

<nav class="pager abs">
  <span class="arrow"></span><span class="current">1</span><span>2</span><span>3</span><span>4</span><span class="arrow"></span>
</nav>

<aside>
  <section class="widget widget-about abs">
    <h4>About Lottchen</h4>
    <p>Morbi ornare gravida elit integer congue augue et malesuada iaculis ipsum dui aliquet felis</p>
    <p>At cursus magna nisl nec elit Praesent elementum elit at tellus nec ultricies sit amet porttitor mattis enim in</p>
    <span class="btn-ghost">Read More</span>
  </section>

  <section class="widget widget-popular abs">
    <div class="widget-head">Popular Articles</div>
    <div class="pop-item"><div class="pop-thumb" role="img" aria-label="Bee in flight" style="background:linear-gradient(135deg,#d9c7a0,#8a6a2a)"></div>
      <div class="pop-text"><h5>Article Tittle here</h5><p>iaculis tempus eros Curabitur vel mi sit amet magna accumsan</p><div class="more">READ MORE</div></div></div>
    <div class="pop-item"><div class="pop-thumb" role="img" aria-label="Snowy branches" style="background:linear-gradient(135deg,#e6eef2,#8aa2b0)"></div>
      <div class="pop-text"><h5>Article Tittle here</h5><p>iaculis tempus eros Curabitur vel mi sit amet magna accumsan</p><div class="more">READ MORE</div></div></div>
    <div class="pop-item"><div class="pop-thumb" role="img" aria-label="Dim room with people" style="background:linear-gradient(135deg,#3a3228,#7a6a52)"></div>
      <div class="pop-text"><h5>Article Tittle here</h5><p>iaculis tempus eros Curabitur vel mi sit amet magna accumsan</p><div class="more">READ MORE</div></div></div>
    <div class="pop-item"><div class="pop-thumb" role="img" aria-label="Dog portrait" style="background:linear-gradient(135deg,#2e2a26,#a88a6a)"></div>
      <div class="pop-text"><h5>Article Tittle here</h5><p>iaculis tempus eros Curabitur vel mi sit amet magna accumsan</p><div class="more">READ MORE</div></div></div>
  </section>

  <section class="widget widget-news abs">
    <h4>Newletter Subscribe</h4>
    <div class="field">Email address</div>
    <div class="btn-fill">Subscribe</div>
  </section>

  <section class="widget widget-tags abs">
    <h4>Henrike's Tags:</h4>
    <div class="tag-list">
      <span>Anthroposophy</span><span>Doctor</span><span>Baby</span><span>Babies</span>
      <span>Featured</span><span>Globuli</span><span>Good Medicine</span><span>Midwife</span>
      <span>Medical</span><span>Practitioner</span><span>Homeopathy</span>
      <span>Vaccination</span><span>Insects</span><span>Pediatrician</span><span>Medicine</span>
      <span>Placebo</span><span>Psychology</span><span>Summer</span><span>Sunscreen</span>
      <span>Animal</span><span>Animal Health</span><span>Nonsense</span>
    </div>
  </section>

  <section class="widget widget-social abs">
    <div class="page-banner" role="img" aria-label="Page cover with cartoon characters">
      <div class="pic"></div>
      <div class="name">Lottchen mag keine…</div>
      <span class="page-btn" style="left:8px">Seite gefällt mir</span>
      <span class="page-btn" style="left:178px">Jetzt einkaufen</span>
    </div>
    <div class="feed-item"><div class="feed-avatar" role="img" aria-label="Reader avatar" style="background:#c8a088"></div>
      <p>Lorem ipsum dolor sit amet inceptos hymenaeos Cum sociis natoque penatibus et magnis dis<small>2 days ago</small></p></div>
    <div class="feed-item"><div class="feed-avatar" role="img" aria-label="Reader avatar" style="background:#8a7a6a"></div>
      <p>Quisque dignissim congue inceptos hymenaeos Cum sociis natoque penatibus et magnis dis parturient montes<small>2 days ago</small></p></div>
  </section>
</aside>

<div class="char char-girl abs" role="img" aria-label="Cartoon girl in a blue dress"></div>
<div class="char char-dog abs" role="img" aria-label="Cartoon brown dog"></div>
<div class="char char-boy abs" role="img" aria-label="Cartoon boy with a red cap"></div>

<svg class="footer-wave abs" viewBox="0 0 1200 90" preserveAspectRatio="none" aria-hidden="true">
  <path d="M0 40 Q600 -20 1200 40 L1200 90 L0 90 Z" fill="var(--green)"/>
  <path d="M0 58 Q600 5 1200 58 L1200 90 L0 90 Z" fill="var(--footer)"/>
</svg>
<footer class="site-footer abs">
  <nav class="foot-nav"><span>Home</span><span>Articles</span><span>About the Henrike</span><span>Henrike's Shop</span><span>Contact</span></nav>
  <p class="copyright">© 2017 Company Name  All right reserved  Term of Use</p>
  <div class="social"><span></span><span></span><span></span><span></span><span></span></div>
</footer>

</body>
</html>
```